Mobile Repair Service on location needs a Web Design

We are starting a new mobile device repair service called Cell Revive and our website needs a design!

Hello Designers!
First, we'd like to make clear this is more than a simple web design contest, we want the designers to create an idea. We want someone who can create the whole theme of the service's we provide. We want someone that can help design our visual branding, help us communicate a sentiment. And we are willing to pay for that.

Who are we?
Our company is based in Rotterdam, the Netherlands. We provide different services for all kinds of electronic devices. The kind of services we provide are, among other things, installations of hardware and software and the repair of broken or malfunctioning devices.
We are starting a new service that offers mobile device repairs on location, be it at the home of our customers, their office, or any other place. Just give us the address and we will come to you for the repair job. This is also our main USP. We have multiple skilled engineers who drive trough the country on a daily basis and can be on location within a working day. Repair is done immediately onsite while the customer waits. At this stage we will start with the smartphone product-group within the mobile devices. In a second phase we might also add tablets.
People don't want to be without their phone for weeks because of some parts that needed to be ordered by a repair center they had to sent their phone to. We offer a fully functional mobile repair center in the form of specially customized vans. These vans have all the tools and utilities needed by our engineers to safely repair your mobile device. Your phone is being repaired directly in front of you, the next business-day, on a location you desire.

For this new service we are creating a website called Cell Revive. The website needs a story and matching design and this is where you come in. We are not looking for a simple template design we can get from any place. We need a story. We want you to create an idea, build a unique theme or vision that helps sell the product/service. This goes beyond the design of the website. We need the whole package, the design you are creating needs to have returning elements like icons, color use, images, maybe even characters etc. You name it! There needs to be a common thread in the design so we can reuse elements in, for example, the email templates, the work order or receipt we give to our customers (we may contact the winner of the contest to design these for us as well!).

The name 'Cell Revive' is chosen. Revive (short for rehabilitate) has a bold and playful tone to it and the design needs to reflect the name. So we're looking for a somewhat playful and cheeky design. Definitely not too serious and definitely modern. We already got a logo that we love and that fit's this description (see attached design documents for the logo). It's bold, powerful and fun. Our web design needs to reflect this as well and has to fit in with our logo.
We would really like it if the design somehow incorporates elements that highlight our unique selling points (repairs on location, we come to you etc.). We would really like some form of story telling in the design. Think clumsy people breaking their phones. Teenagers in tears because they have no access to their friends. People nowadays have the need to always be 'connected'. What happens when your phone is broken or malfunctioning? We're handling tech, we are nerds and a little bit weird, but we're professionals and here to help you with your problem. The sentiment Byte Troop tries to communicate is something we really like. We're looking for fresh idea's, anything goes!

In an overview all Unique Selling Points of the Cell revive service:
- Professional service on location. Don’t ship to us we will come to you!
- Clear pricing upfront. No hidden cost.
- Next business-day repair.
- Backed by a professional call center open 12 hours a day and open on a Saturday as well
- Backed by a professional repair center with more then 12 years of experience
- Repair is done by certified engineers
- 1 year warranty on the repair

The process:
The main function of our website will be for customers to make a repair request. A customer will visit our website and can make a repair request immediately by going through a 'request-order-flow'. In this flow he or she will need to fill in some forms and can select wich type/model/brand of mobile device he or she has and what parts need to be repaired. After a request is placed we will call the customer back (within an hour) for a short intake and to set a date/time and location. Our engineer will meet the customer at the specified location and will repair the device onsite in one of our mobile repair centers, which is a specialized van equipped with all the tools needed for device restorations.
So in short the steps are:
- Choose your device and repair job
- Place the order
- Get a callback within the hour
- Set date and location
- We will come to you.

Website functionality:
Our website is our main form of communication. So the sentiment we want to communicate needs be reflected in the design. We need a main/front page designed (preferably a long scrolling page design) containing:
1. Customers will be able to request a repair job directly on our website. So there will need to be a prominent button/link at the top of our main page that will bring the customer to this 'request-order-flow'. This is the main flow which needs to be full focus on the front page. All other items are secondary.
2. The general information of who we are and what we do, and why the customer should choose us. Preferably in short bullet-point type keywords/sentences with icons or other visual cues. See our unique selling points to get an idea of the information that will be displayed here.
3. There needs to be a section that will explain the process (see above) of a repair request step-by- step, again in brief short key sentences and with (custom) icons.
4. There needs to be a section that explains to the customer he/she can always contact us if they are not sure what the problem is with their device, and for this reason are not sure what repair request they should order.
5. We want to implement some functionality that display customer ratings or customer reviews. So there needs to be room for some kind of widget of plugin we're going to implement which shows these reviews.
6. A 'For business section' where we will explain all the options we provide for corporate clients.
7. Social media links.
8. There needs to be a menu with buttons that leads to the all sections described in the previous points.

For now, we need a design for our front page. In the second phase, when we have picked our winner, we may ask the winner to design the page(s) for our request workflow as well.

EDIT:
Finally, we have a very specific order in mind for the different segments of our website. We would like you to add some more segments that were not in our original brief as well:

1. Top header with order/request button. (should instantly make clear our main USP, we do repairs on location)
2. Our process
3. Our unique selling points / why choose us
4. The kind of repairs we do (broken screens, broken batteries, water damage, broken camera's, no sound etc.)
5. A 'meet our team' section, where we introduce some of our engineers
6. A 'contact us for any questions' section/
7. Testimonials/user reviews
8. A section where we show key performance indicators
9. 'For businesses' sections
10.'Subscribe for newsletter' field
11. Social media buttons
Updates

Industry/Entity Type

It Service

Number of Pages Required

1 page

Font styles to use
Sans Serif

Requirements
Must have
• a main/front page, design only
• custom icons/images for banners, adverts online and in print (high res)
Nice to have
• Storytelling in our design.
• Design that fits with our brand new logo.
• Elements like icons to have a flat design.
• Keep in mind that the website will need to be responsive when designing! (Ideally provide an example of the mobile design as well)
• Create a fun and trustworthy feeling.

```html
<!DOCTYPE html>
<html lang="en">
<head>
<meta charset="utf-8">
<title>Cell Revive – Mobile Repair On Location</title>
<link href="https://fonts.googleapis.com/css2?family=Open+Sans:wght@400;600;700;800&display=swap" rel="stylesheet">
<style>
:root{
  --orange:#e2561b;
  --orange-dark:#c9470f;
  --ink:#222222;
  --body:#555555;
  --muted:#8a8a8a;
  --stat:#6d6d6d;
  --black:#111111;
  --panel:#1a1a1a;
  --light:#f5f5f5;
  --footer:#3b3b3b;
  --white:#ffffff;
  --lavender:#d8d6ef;
}
*{box-sizing:border-box;margin:0;padding:0}
html,body{width:1200px;height:3689px;overflow:hidden}
body{font-family:"Open Sans",Arial,sans-serif;color:var(--body);background:var(--white);position:relative}
.section-title{font-size:22px;font-weight:700;color:var(--ink);text-align:center}
.section-title::after{content:"";display:block;width:52px;height:3px;background:var(--orange);margin:10px auto 0}
.section-title.light{color:var(--white)}

/* Hero */
.hero{position:absolute;top:0;left:0;width:1200px;height:438px}
.hero-photo{position:absolute;inset:0;background:linear-gradient(160deg,#3b3d40 0%,#565a5e 35%,#2a2b2d 70%,#4a3c33 100%)}
.hero-shade{position:absolute;inset:0;background:rgba(0,0,0,.35)}
.brand{position:absolute;left:184px;top:20px;display:flex;align-items:center;gap:10px}
.brand-dot{width:34px;height:34px;border-radius:50%;background:var(--orange)}
.brand-name{color:var(--white);font-weight:800;font-size:17px;line-height:18px;width:70px}
.main-nav{position:absolute;right:184px;top:32px;display:flex;gap:22px}
.main-nav a{color:var(--white);text-decoration:none;font-size:12px;font-weight:700;letter-spacing:.2px}
.hero-title{position:absolute;top:140px;left:0;width:100%;text-align:center;color:var(--white);font-size:31px;font-weight:700;line-height:38px}

/* Enquiry */
.enquiry{position:absolute;left:184px;top:315px;width:832px;height:275px;background:var(--panel);padding:24px 40px}
.enquiry-title{font-size:22px;font-weight:600;color:var(--white);text-transform:uppercase}
.enquiry-title span{color:var(--orange);text-transform:none}
.enquiry-grid{display:grid;grid-template-columns:repeat(3,1fr);gap:14px 14px;margin-top:20px}
.field{height:30px;border:1px solid var(--orange);color:#ccc;font-size:11px;padding:7px 8px;position:relative}
.field.wide{grid-column:1/4;height:50px}
.field svg{position:absolute;right:7px;top:7px}
.enquiry-foot{display:flex;align-items:center;justify-content:space-between;margin-top:18px}
.terms{color:var(--orange);font-size:10px;width:240px}
.send-btn{background:var(--orange);color:var(--white);font-size:12px;font-weight:700;border-radius:16px;width:118px;height:30px;display:flex;align-items:center;justify-content:center}
.quick-call{color:var(--white);font-size:13px;font-weight:700;width:240px;text-align:right}

/* Who */
.who{position:absolute;top:438px;left:0;width:1200px;height:1013px}
.who .section-title{position:absolute;top:250px;width:100%}
.who-text{position:absolute;left:184px;top:332px;width:476px;font-size:11.5px;line-height:18px}
.who-lead{font-size:14px;font-weight:700;color:var(--ink);line-height:20px;margin-bottom:14px}
.who-lead span{color:var(--orange);font-weight:400;font-size:12px}
.who-text p{margin-bottom:14px}
.warranty-box{position:absolute;left:684px;top:332px;width:332px;height:263px;border:1px solid #dcdcdc;display:flex;align-items:center;justify-content:center}
.warranty-art{width:140px;height:190px;background:radial-gradient(circle at 50% 40%,#f06a2a 0%,#e2561b 45%,#c64510 100%);border-radius:70px 70px 8px 8px}
.usp-grid{position:absolute;left:184px;top:681px;width:832px;display:grid;grid-template-columns:repeat(3,1fr);row-gap:42px}
.usp{display:flex;gap:14px;width:250px}
.usp-icon{flex:none;width:74px;height:74px;border:2px solid var(--orange);display:flex;align-items:center;justify-content:center}
.usp h3{font-size:12px;font-weight:700;color:var(--ink);line-height:15px;text-transform:uppercase;margin:2px 0 6px}
.usp p{font-size:10.5px;line-height:15px}

/* Process */
.process{position:absolute;top:1451px;left:0;width:1200px;height:622px;overflow:hidden}
.process-photo{position:absolute;inset:0;background:linear-gradient(135deg,#3a3a3a 0%,#5a5148 40%,#2e2e2e 75%,#4b4b4b 100%)}
.process-shade{position:absolute;inset:0;background:rgba(0,0,0,.5)}
.process .section-title{position:absolute;top:54px;width:100%}
.process-intro{position:absolute;top:108px;left:260px;width:680px;text-align:center;color:var(--white);font-size:11px;line-height:16px}
.step-circle{position:absolute;border:2px solid var(--white);border-radius:50%;display:flex;align-items:center;justify-content:center}
.step-label{position:absolute;top:372px;color:var(--orange);font-size:12px;font-weight:600;text-align:center;width:140px}
.step-num{position:absolute;top:405px;width:22px;height:22px;border-radius:50%;background:var(--orange);color:var(--white);font-size:11px;font-weight:700;display:flex;align-items:center;justify-content:center}
.step-line{position:absolute;top:416px;left:306px;width:590px;border-top:1px dashed var(--orange)}
.process-outro{position:absolute;top:505px;left:260px;width:680px;text-align:center;color:var(--white);font-size:11px;line-height:16px}

/* Testimonials */
.reviews{position:absolute;top:2073px;left:0;width:1200px;height:447px;background:var(--light)}
.reviews .section-title{position:absolute;top:62px;width:100%}
.quote-box{position:absolute;left:184px;top:140px;width:832px;height:99px;border:2px solid #d0d0d0;background:var(--white);padding:22px 70px;text-align:center;font-size:11px;line-height:16px}
.quote-mark{position:absolute;left:14px;top:10px}
.avatars{position:absolute;top:270px;left:0;width:100%;display:flex;justify-content:center;align-items:center;gap:22px}
.avatar{width:58px;height:58px;border-radius:50%;background:radial-gradient(circle at 50% 40%,#bdbdbd,#7e7e7e)}
.avatar.active{width:80px;height:80px;border:3px solid var(--orange)}
.reviewer{position:absolute;top:350px;width:100%;text-align:center}
.reviewer strong{display:block;color:var(--orange);font-size:11px}
.reviewer span{font-size:11px;color:var(--body)}

/* Call band */
.call-band{position:absolute;top:2520px;left:0;width:1200px;height:254px;background:linear-gradient(180deg,#e55d1f,#d34d14);text-align:center;color:var(--white)}
.call-kicker{position:absolute;top:62px;width:100%;font-size:21px;font-weight:700}
.call-number{position:absolute;top:96px;width:100%;font-size:52px;font-weight:800;line-height:60px}
.call-text{position:absolute;top:164px;left:300px;width:600px;font-size:11px;line-height:16px}

/* Stats */
.stats{position:absolute;top:2774px;left:184px;width:832px;height:214px;display:flex;align-items:center}
.stat{flex:1;text-align:center;border-left:1px solid #d8d8d8}
.stat:first-child{border-left:none}
.stat b{display:block;font-size:44px;font-weight:800;color:var(--stat);line-height:50px}
.stat span{font-size:11px;color:var(--orange);text-transform:uppercase}

/* Map */
.map{position:absolute;top:2988px;left:0;width:1200px;height:344px;background:linear-gradient(180deg,#e4e4e4,#d6d6d6)}
.map-pin{position:absolute;left:645px;top:132px}

/* CTA */
.cta{position:absolute;top:3332px;left:0;width:1200px;height:106px;background:var(--black)}
.cta-text{position:absolute;left:236px;top:30px;color:var(--white)}
.cta-text h2{font-size:20px;font-weight:600;line-height:24px}
.cta-text p{font-size:15px;line-height:20px}
.cta-btn{position:absolute;left:733px;top:36px;width:172px;height:40px;background:var(--lavender);color:var(--black);font-size:14px;font-weight:700;display:flex;align-items:center;justify-content:center}

/* Footer */
.footer{position:absolute;top:3438px;left:0;width:1200px;height:251px;background:var(--footer)}
.footer-col{position:absolute;top:52px;color:var(--white)}
.footer-col h4{font-size:12px;font-weight:700;text-transform:uppercase;margin-bottom:10px}
.footer-col h4::after{content:"";display:block;width:24px;height:2px;background:var(--orange);margin-top:5px}
.footer-col li{list-style:none;font-size:11px;line-height:24.5px;display:flex;align-items:center;gap:8px}
.footer-brand{position:absolute;left:770px;top:80px;display:flex;align-items:center;gap:10px}
.footer-brand .brand-dot{width:44px;height:44px}
.footer-brand .brand-name{font-size:19px;line-height:21px;width:90px}
</style>
</head>
<body>

<header class="hero">
  <div class="hero-photo" role="img" aria-label="Close-up of hands repairing an opened smartphone on a work mat with tools"></div>
  <div class="hero-shade"></div>
  <div class="brand"><span class="brand-dot"></span><span class="brand-name">CELL REVIVE</span></div>
  <nav class="main-nav">
    <a href="#">HOME</a><a href="#">WHO WE'RE</a><a href="#">WHAT WE DO</a><a href="#">WHY CUSTOMERS CHOOSE US</a><a href="#">CONTACT</a>
  </nav>
  <h1 class="hero-title">Your phone is being repaired<br>directly in front of you</h1>
</header>

<section class="enquiry">
  <h2 class="enquiry-title">Send us enquiry! <span>we will come to you!</span></h2>
  <div class="enquiry-grid">
    <div class="field">Select Device</div>
    <div class="field">Full name</div>
    <div class="field">Email Address</div>
    <div class="field">Contact #</div>
    <div class="field">Select Date
      <svg width="14" height="14" viewBox="0 0 14 14" fill="none" stroke="#aaa"><rect x="1.5" y="2.5" width="11" height="10"/><line x1="1.5" y1="5.5" x2="12.5" y2="5.5"/></svg></div>
    <div class="field">Choose Time
      <svg width="14" height="14" viewBox="0 0 14 14" fill="none" stroke="#aaa"><circle cx="7" cy="7" r="5.5"/><path d="M7 4v3l2 1.5"/></svg></div>
    <div class="field wide">Address / Detail</div>
  </div>
  <div class="enquiry-foot">
    <span class="terms">Terms &amp; Condition</span>
    <span class="send-btn">Send Us</span>
    <span class="quick-call">Quick Call: 010-482-937</span>
  </div>
</section>

<section class="who">
  <h2 class="section-title">Who we're</h2>
  <div class="who-text">
    <p class="who-lead">Lorem ipsum dolor sit amet, consectetur adipiscing elit. <span>Curabitur vitae eros a lectus auctor varius. Nullam id urna nec eros faucibus dignissim ac sit amet erat.</span></p>
    <p>Curabitur risus magna, pulvinar sed nisl et, sodales fermentum erat. Maecenas ornare elit vitae tortor vestibulum commodo. Nam eros leo, placerat ac scelerisque vitae, facilisis a ante. Donec a augue luctus, vehicula nisl vel, condimentum felis. Phasellus id tellus posuere, ultrices metus ut, lacinia massa. Curabitur fermentum tincidunt congue. Interdum et malesuada fames ac ante ipsum primis in faucibus</p>
    <p>At Auto, we understand car maintenance and repair services goes hand in hand with the purchase of any vehicle. Starting as a family business with just two people in October 1956, we have built and made our reputation</p>
  </div>
  <div class="warranty-box">
    <div class="warranty-art" role="img" aria-label="Orange one-year repair warranty ribbon badge"></div>
  </div>

  <div class="usp-grid">
    <div class="usp">
      <div class="usp-icon"><svg width="40" height="40" viewBox="0 0 40 40" fill="none" stroke="#e2561b" stroke-width="2"><circle cx="20" cy="20" r="7"/><circle cx="20" cy="20" r="14" stroke-dasharray="5 4"/></svg></div>
      <div><h3>Professional service on location</h3><p>Professional service on location. Don't ship to us we will come to you!</p></div>
    </div>
    <div class="usp">
      <div class="usp-icon"><svg width="40" height="40" viewBox="0 0 40 40" fill="none" stroke="#e2561b" stroke-width="2"><path d="M8 20 L20 8 H32 V20 L20 32 Z"/><circle cx="26" cy="14" r="2"/><text x="14" y="24" font-size="9" fill="#e2561b" stroke="none" font-family="Open Sans,sans-serif">$</text></svg></div>
      <div><h3>Clear pricing</h3><p>Clear pricing upfront. No hidden cost.</p></div>
    </div>
    <div class="usp">
      <div class="usp-icon"><svg width="40" height="40" viewBox="0 0 40 40" fill="none" stroke="#e2561b" stroke-width="2"><circle cx="20" cy="22" r="12"/><path d="M20 15v7l5 3M16 6h8"/></svg></div>
      <div><h3>Next business day repair</h3><p>Nam eros leo, placerat ac scelerisque vitae, facilisis a ante.</p></div>
    </div>
    <div class="usp">
      <div class="usp-icon"><svg width="40" height="40" viewBox="0 0 40 40" fill="none" stroke="#e2561b" stroke-width="2"><path d="M9 24v-5a11 11 0 0 1 22 0v5"/><rect x="7" y="22" width="5" height="9" rx="2"/><rect x="28" y="22" width="5" height="9" rx="2"/><path d="M31 31c0 3-4 4-8 4"/></svg></div>
      <div><h3>Lorem ispum dollor amet</h3><p>Backed by a professional call center open 12 hours a day and open on a Saturday as well</p></div>
    </div>
    <div class="usp">
      <div class="usp-icon"><svg width="40" height="40" viewBox="0 0 40 40" fill="none" stroke="#e2561b" stroke-width="2"><path d="M9 19a11 11 0 0 1 22 0z"/><line x1="6" y1="19" x2="34" y2="19"/><path d="M12 34c1-6 4-8 8-8s7 2 8 8"/></svg></div>
      <div><h3>Lorem ispum dollor amet</h3><p>Backed by a professional repair center with more then 12 years of experience</p></div>
    </div>
    <div class="usp">
      <div class="usp-icon"><svg width="40" height="40" viewBox="0 0 40 40" fill="none" stroke="#e2561b" stroke-width="2"><circle cx="20" cy="20" r="13" stroke-dasharray="6 3"/><path d="M14 20l4 4 8-8"/></svg></div>
      <div><h3>Repair is done</h3><p>Repair is done by certified engineers</p></div>
    </div>
  </div>
</section>

<section class="process">
  <div class="process-photo" role="img" aria-label="Engineers in hard hats working around a table with a laptop"></div>
  <div class="process-shade"></div>
  <h2 class="section-title light">What we do</h2>
  <p class="process-intro">Lorem ipsum dolor sit amet, consectetur adipiscing elit. Curabitur vitae eros a lectus auctor varius. Nullam id urna nec eros faucibus dignissim ac sit amet erat. Curabitur risus magna, pulvinar sed nisl et, sodales fermentum erat.</p>

  <div class="step-circle" style="left:262px;top:233px;width:94px;height:94px">
    <svg width="40" height="40" viewBox="0 0 40 40" fill="none" stroke="#fff" stroke-width="2"><circle cx="20" cy="14" r="7"/><path d="M6 36c1-8 7-12 14-12s13 4 14 12"/></svg></div>
  <div class="step-circle" style="left:384px;top:233px;width:94px;height:94px">
    <svg width="40" height="44" viewBox="0 0 40 44" fill="none" stroke="#fff" stroke-width="2"><path d="M8 3h18l8 8v30H8z"/><path d="M14 16h3M20 16h9M14 23h3M20 23h9M14 30h3M20 30h9"/></svg></div>
  <div class="step-circle" style="left:526px;top:206px;width:148px;height:148px">
    <svg width="70" height="70" viewBox="0 0 70 70" fill="none" stroke="#fff" stroke-width="3"><path d="M14 56 L44 26"/><circle cx="50" cy="20" r="9"/><path d="M14 14 L56 56"/><path d="M8 10 l6 -4 6 6 -4 6z"/></svg></div>
  <div class="step-circle" style="left:706px;top:233px;width:94px;height:94px">
    <svg width="42" height="42" viewBox="0 0 42 42" fill="none" stroke="#fff" stroke-width="2"><rect x="5" y="8" width="28" height="28"/><path d="M12 20l7 8 18-22"/></svg></div>
  <div class="step-circle" style="left:852px;top:248px;width:86px;height:86px">
    <svg width="40" height="30" viewBox="0 0 40 30" fill="none" stroke="#fff" stroke-width="2"><rect x="3" y="5" width="34" height="20" rx="2"/><circle cx="20" cy="15" r="5"/></svg></div>

  <span class="step-label" style="left:230px">Customer Request</span>
  <span class="step-label" style="left:362px">Enquiry Listed</span>
  <span class="step-label" style="left:530px">Request Processed</span>
  <span class="step-label" style="left:693px">Reuqest Done</span>
  <span class="step-label" style="left:825px">Feedback</span>
  <div class="step-line"></div>
  <span class="step-num" style="left:289px">1</span>
  <span class="step-num" style="left:420px">2</span>
  <span class="step-num" style="left:589px">3</span>
  <span class="step-num" style="left:753px">4</span>
  <span class="step-num" style="left:884px">5</span>

  <p class="process-outro">Lorem ipsum dolor sit amet, consectetur adipiscing elit. Curabitur vitae eros a lectus auctor varius. Nullam id urna nec eros faucibus dignissim ac sit amet erat. Curabitur risus magna, pulvinar sed nisl et, sodales fermentum erat. Maecenas ornare elit vitae tortor vestibulum commodo. Nam eros leo, placerat ac scelerisque vitae, facilisis a ante. Donec a augue luctus, vehicula nisl vel, condimentum felis. Phasellus id tellus posuere, ultrices</p>
</section>

<section class="reviews">
  <h2 class="section-title">Satisfied Customers</h2>
  <div class="quote-box">
    <svg class="quote-mark" width="44" height="36" viewBox="0 0 44 36" fill="#cfcfcf"><path d="M2 34V18C2 9 7 3 16 1l2 4c-5 2-8 6-8 11h8v18zM24 34V18c0-9 5-15 14-17l2 4c-5 2-8 6-8 11h8v18z"/></svg>
    Sed at enim commodo, vulputate tellus vel, fermentum libero. Nulla vehicula volutpat iaculis. Nunc semper accumsan nisi eget lacinia urna lobortis sit amet. Praesent et luctus magna. Donec tincidunt enim bibendum metus sagittis, sit amet rutrum nisl semper. Morbi orci eros, consectetur quis tincidunt quis, aliquam sed diam. Interdum et malesuada fames ac ante ipsum primis in faucibus.
  </div>
  <div class="avatars">
    <div class="avatar" role="img" aria-label="Customer portrait"></div>
    <div class="avatar" role="img" aria-label="Customer portrait"></div>
    <div class="avatar active" role="img" aria-label="Portrait of the featured customer"></div>
    <div class="avatar" role="img" aria-label="Customer portrait"></div>
    <div class="avatar" role="img" aria-label="Customer portrait"></div>
  </div>
  <div class="reviewer"><strong>JOHN DOE</strong><span>Marketing Manager</span></div>
</section>

<section class="call-band">
  <p class="call-kicker">Need Quick help?</p>
  <p class="call-number">Call Us:&nbsp; 010-482-937</p>
  <p class="call-text">Lorem ipsum dolor sit amet, consectetur adipiscing elit. Curabitur vitae eros a lectus auctor varius. Nullam id urna nec eros faucibus dignissim ac sit amet erat. Curabitur risus magna, pulvinar sed nisl et, sodales</p>
</section>

<section class="stats">
  <div class="stat"><b>40</b><span>Branches</span></div>
  <div class="stat"><b>145</b><span>Company Staff</span></div>
  <div class="stat"><b>1268</b><span>Customers</span></div>
  <div class="stat"><b>12</b><span>Years Experience</span></div>
</section>

<section class="map" role="img" aria-label="Greyscale street map of the service area with a location pin">
  <svg class="map-pin" width="24" height="36" viewBox="0 0 24 36"><path d="M12 1a11 11 0 0 0-11 11c0 8 11 23 11 23s11-15 11-23A11 11 0 0 0 12 1z" fill="#666"/><circle cx="12" cy="12" r="4" fill="#d9d9d9"/></svg>
</section>

<section class="cta">
  <div class="cta-text">
    <h2>WANT TO REPAIR YOUR SMARTPHONE?</h2>
    <p>We're here to help you manage your problem.</p>
  </div>
  <span class="cta-btn">SEND REQUEST</span>
</section>

<footer class="footer">
  <div class="footer-col" style="left:184px">
    <h4>Important Links</h4>
    <ul><li>Phone Repair Service 1</li><li>Phone Repair Service 2</li><li>Phone Repair Service 3</li><li>Phone Repair Service 4</li><li>Phone Repair Service 5</li></ul>
  </div>
  <div class="footer-col" style="left:391px">
    <h4>Website Link</h4>
    <ul><li>Phone Repair Service 1</li><li>Phone Repair Service 2</li><li>Phone Repair Service 3</li><li>Phone Repair Service 4</li><li>Phone Repair Service 5</li></ul>
  </div>
  <div class="footer-col" style="left:617px">
    <h4>Website Link</h4>
    <ul><li>Chatterbook</li><li>Chirpline</li><li>Workwire</li></ul>
  </div>
  <div class="footer-brand"><span class="brand-dot"></span><span class="brand-name">CELL REVIVE</span></div>
</footer>

</body>
</html>
```